Fence Flyer to Attract More Sales During Winter

We need a new flyer made that we can distribute to residential mailboxes. The flyer is to promote our Frostline Picket Days. We like simply designs, and we would like the flyer to showcase a lot of our fence photos. More of our photos are online at our website at www.getbramblerail.com - our new address needs to also be featured on the flyer - 436 Quillen rd, Monroe, NC 28117. I do want the words "FROSTLINE PICKET DAYS" to be dominate on the flyer with the description "Wood fences starting at $12/FT!" Please look through our Facebook page and our website to gather more photos or information. We are flexible on colors, nothing to fancy - simple flyer design please.

Target Market(s)

Residential homeowners that need a new fence to enclose their yard for safety, security or decorative

Industry/Entity Type

Residential Construction

Font styles to use
Sans Serif

Colors

Designer to choose colors to be used in the design.

Requirements
Must have
• Frostline Picket Days
• Contact information for the business
• "Come visit our outdoor showroom, open 24/7!"
Nice to have
• Photos of our fences - you can find more on our website at www.GetBrambleRail.com or Facebook.com/MeadowlarkRailGPV
Should not have
• Flashy designs

```html
<!DOCTYPE html>
<html lang="en">
<head>
<meta charset="utf-8">
<title>Frostline Picket Days Flyer</title>
<link href="https://fonts.googleapis.com/css2?family=Bungee+Inline&family=Montserrat:wght@400;500;600;700&family=Alfa+Slab+One&family=Roboto+Slab:wght@400;600&display=swap" rel="stylesheet">
<style>
  :root {
    --stage: #e9e9eb;
    --paper: #ffffff;
    --sky: #2f8fd8;
    --sky-soft: #8fc0e6;
    --tile: #eeeff1;
    --ink: #2b2b2b;
    --red: #e8141c;
    --photo-metal-a: #5a5d55;
    --photo-metal-b: #7f8a6c;
    --photo-wood-a: #c9ad7c;
    --photo-wood-b: #e0cda3;
    --photo-soil-a: #9a5a38;
    --photo-soil-b: #6b4b34;
  }
  * { box-sizing: border-box; margin: 0; padding: 0; }
  html, body { width: 1200px; height: 900px; overflow: hidden; background: var(--stage); }
  .flyer {
    position: absolute; left: 300px; top: 26px; width: 600px; height: 848px;
    background: var(--paper); overflow: hidden;
    font-family: "Montserrat", sans-serif; color: var(--ink);
    box-shadow: 0 6px 24px rgba(0,0,0,.12);
  }
  .hero-photo {
    position: absolute; left: 0; top: 0; width: 600px; height: 430px;
    background: linear-gradient(160deg, var(--photo-metal-a), var(--photo-metal-b) 70%, #9aa07e);
    clip-path: polygon(0 0, 100% 0, 100% 100%, 0 46%);
  }
  .brand { position: absolute; left: 26px; top: 20px; display: flex; align-items: flex-start; gap: 10px; color: #fff; }
  .brand-mark { width: 34px; height: 34px; background: #fff; margin-top: 2px; }
  .brand-name { font-size: 19px; font-weight: 600; line-height: 1.1; }
  .brand-phone { font-size: 17px; font-weight: 600; line-height: 1.2; }
  .brand-tagline { font-size: 8px; font-weight: 500; letter-spacing: .3px; opacity: .9; }
  .tile { position: absolute; background: var(--tile); border-radius: 10px; }
  .chip { position: absolute; background: var(--sky-soft); }
  .frame {
    position: absolute; background: var(--paper); border-radius: 26px; padding: 10px;
    box-shadow: 0 4px 14px rgba(0,0,0,.12);
  }
  .frame .photo { width: 100%; height: 100%; border-radius: 22px; }
  .frame-wood { left: 34px; top: 150px; width: 230px; height: 232px; }
  .frame-wood .photo { background: linear-gradient(150deg, var(--photo-wood-b), var(--photo-wood-a)); }
  .frame-build { left: 276px; top: 214px; width: 176px; height: 176px; }
  .frame-build .photo { background: linear-gradient(140deg, #b8b39f, var(--photo-wood-a)); }
  .frame-metal { left: 368px; top: 398px; width: 206px; height: 210px; }
  .frame-metal .photo { background: linear-gradient(160deg, var(--photo-soil-a), var(--photo-soil-b)); }
  .headline { position: absolute; left: 36px; top: 432px; }
  .headline-top { font-family: "Bungee Inline", sans-serif; font-size: 50px; color: var(--sky); line-height: 1; }
  .headline-mid { font-size: 46px; font-weight: 500; line-height: 1.05; margin-left: 60px; }
  .headline-bottom { font-family: "Alfa Slab One", serif; font-size: 78px; color: var(--red); line-height: 1; margin-left: 40px; }
  .offer {
    position: absolute; left: 26px; top: 652px; display: flex; align-items: stretch;
    font-size: 17px; font-weight: 500; color: #fff;
  }
  .offer-text { background: var(--sky); padding: 6px 10px; }
  .offer-price { background: var(--red); padding: 6px 8px; font-weight: 600; }
  .rule { position: absolute; left: 20px; top: 708px; width: 350px; height: 2px; background: var(--sky-soft); }
  .address { position: absolute; left: 24px; top: 726px; display: flex; align-items: center; gap: 10px; font-family: "Roboto Slab", serif; font-size: 16px; }
  .call { position: absolute; left: 230px; top: 772px; text-align: left; }
  .call-label { font-size: 12px; font-weight: 700; }
  .call-phone { font-size: 20px; font-weight: 700; color: var(--sky); }
  .showroom { position: absolute; left: 398px; top: 642px; width: 190px; text-align: center; }
  .showroom-lead { font-family: "Roboto Slab", serif; font-weight: 600; font-size: 15px; line-height: 1.25; }
  .showroom-hours {
    margin-top: 8px; background: var(--sky-soft); padding: 10px 4px;
    font-family: "Alfa Slab One", serif; color: var(--red); font-size: 22px;
  }
  .corner { position: absolute; right: 0; bottom: 0; }
</style>
</head>
<body>
  <main class="flyer">
    <div class="hero-photo" role="img" aria-label="Black aluminum fence and arched gate in a backyard"></div>

    <div class="brand">
      <span class="brand-mark"></span>
      <div>
        <div class="brand-name">Bramble Rail</div>
        <div class="brand-phone">704-555-0163</div>
        <div class="brand-tagline">Quality fences built for lasting homes</div>
      </div>
    </div>

    <div class="tile" style="left:230px;top:360px;width:70px;height:56px"></div>
    <div class="tile" style="left:300px;top:400px;width:60px;height:60px"></div>
    <div class="tile" style="left:340px;top:470px;width:80px;height:70px"></div>
    <div class="tile" style="left:390px;top:600px;width:70px;height:40px"></div>
    <div class="tile" style="left:520px;top:606px;width:60px;height:40px"></div>
    <div class="chip" style="left:272px;top:190px;width:24px;height:24px"></div>
    <div class="chip" style="left:14px;top:278px;width:22px;height:40px"></div>
    <div class="chip" style="left:356px;top:500px;width:28px;height:26px"></div>
    <div class="chip" style="left:560px;top:540px;width:26px;height:30px"></div>
    <div class="chip" style="left:392px;top:612px;width:22px;height:22px"></div>

    <div class="frame frame-wood"><div class="photo" role="img" aria-label="New wooden privacy fence with gate"></div></div>
    <div class="frame frame-build"><div class="photo" role="img" aria-label="Installer nailing boards on a wood fence"></div></div>
    <div class="frame frame-metal"><div class="photo" role="img" aria-label="Black metal fence along fresh red soil"></div></div>

    <h1 class="headline">
      <div class="headline-top">FROSTLINE</div>
      <div class="headline-mid">Picket</div>
      <div class="headline-bottom">DAYS</div>
    </h1>

    <p class="offer"><span class="offer-text">"Wood fences starting at</span><span class="offer-price">$12/FT!"</span></p>

    <div class="rule"></div>

    <p class="address">
      <svg width="14" height="20" viewBox="0 0 14 20" aria-hidden="true"><path d="M7 0C3.1 0 0 3.1 0 7c0 5 7 13 7 13s7-8 7-13c0-3.9-3.1-7-7-7zm0 9.5A2.5 2.5 0 1 1 7 4.5a2.5 2.5 0 0 1 0 5z" fill="#2b2b2b"/></svg>
      436 Quillen rd, Monroe, NC 28117
    </p>

    <div class="call">
      <div class="call-label">CALL US!</div>
      <div class="call-phone">704-555-0163</div>
    </div>

    <div class="showroom">
      <p class="showroom-lead">Come Visit<br>Our<br>Outdoor Showroom</p>
      <p class="showroom-hours">"Open 24/7!"</p>
    </div>

    <svg class="corner" width="90" height="70" viewBox="0 0 90 70" aria-hidden="true"><polygon points="90,0 90,70 0,70" fill="#8fc0e6"/></svg>
  </main>
</body>
</html>
```